Business Postcard Design for Personal Training Company

Need a postcard design for my company called "Maple Stride" Colors are Navy Blue, Blue, Grey and White.

On the front I want there to be pictures and it to feature a box that says "Free Consultation + 50% off your first session!"

And somehow to feature the following phrases " Lose Weight. Gain Muscle."
"Customized Personal training using Q-Pulse, the latest technology in fitness. Reach your fitness goals in just two 25-min sessions per week"

Also want featured the following phrases (maybe on back):

"up to 18 times more effective than a conventional gym workout"

I need the back of the postcard to have all my business information:

Address: 372 Dovercrest Ave, Building B Suite 218, Costa Mesa CA 92631
Website: maple-stride.example
Phone #: (949) 555-0137
E-mail: maplestridehealth@mailbox.example

I am going to upload my logo, before and after pictures and pictures of people training on the device. Feel free to use as many/or little photos as you want.

Target Market(s)

Wealthy Adults 40+ years old looking for a personal trainer

Industry/Entity Type

Personal Trainer

Colors
0455a3
85cae6
aaaaaa
ffffff

Requirements
Must have
• At least two of the before and after photos, and two or more photos of people working out on the device.

```html
<!DOCTYPE html>
<html lang="en">
<head>
<meta charset="utf-8">
<title>Maple Stride Postcard</title>
<link href="https://fonts.googleapis.com/css2?family=Lato:ital,wght@0,300;0,400;0,700;1,300&display=swap" rel="stylesheet">
<style>
  :root {
    --navy: #0455a3;
    --blue: #1b8fc9;
    --blue-deep: #0a7dbb;
    --sky: #85cae6;
    --headline: #2a9fd6;
    --grey: #aaaaaa;
    --band: #4a4a4c;
    --ink: #333333;
    --white: #ffffff;
    --backdrop: #e9ecef;
  }
  * { box-sizing: border-box; margin: 0; padding: 0; }
  html, body { width: 1200px; height: 1200px; overflow: hidden; }
  body {
    background: var(--backdrop);
    font-family: "Lato", sans-serif;
    color: var(--ink);
    position: relative;
  }
  .postcard {
    position: absolute;
    left: 242px;
    width: 717px;
    height: 556px;
    background: var(--white);
    overflow: hidden;
    box-shadow: 0 4px 14px rgba(0,0,0,0.18);
  }
  .postcard--front { top: 28px; }
  .postcard--back { top: 616px; }
  .abs { position: absolute; }

  .tagline-band {
    position: absolute;
    left: 0; right: 0; bottom: 0;
    height: 62px;
    background: var(--band);
    color: var(--white);
    font-style: italic;
    font-weight: 300;
    font-size: 21px;
    display: flex; align-items: center; justify-content: center;
  }

  /* front */
  .front-shape { position: absolute; left: 0; top: 0; }
  .front-copy {
    position: absolute; left: 20px; top: 36px; width: 430px;
    text-align: center;
  }
  .offer {
    color: var(--headline);
    font-weight: 300;
    font-size: 27px;
    line-height: 32px;
  }
  .offer strong { font-weight: 700; color: var(--blue-deep); }
  .slogan { margin-top: 26px; font-size: 31px; font-weight: 300; color: #333; }
  .intro { margin-top: 8px; font-size: 15px; font-weight: 300; line-height: 20px; color: #555; }
  .goals { margin-top: 24px; font-size: 21px; font-weight: 300; line-height: 26px; color: #444; }
  .goals .accent { color: var(--headline); }
  .goals strong { color: var(--blue-deep); font-weight: 700; }

  .brand {
    display: flex; align-items: center; gap: 8px;
    color: var(--navy); font-weight: 700; font-size: 17px; letter-spacing: 1px;
  }
  .brand-dot { width: 16px; height: 16px; border-radius: 50%; background: var(--sky); }
  .brand--front { left: 148px; top: 376px; }

  .contact { left: 32px; top: 424px; }
  .contact .label { font-size: 13px; color: #555; text-decoration: underline; font-weight: 300; }
  .contact .phone { font-size: 21px; color: var(--blue-deep); margin-top: 2px; }
  .contact .mail { font-size: 13px; color: #555; font-weight: 300; }
  .social { left: 282px; top: 457px; display: flex; gap: 4px; }
  .social span { width: 22px; height: 22px; border-radius: 50%; background: var(--navy); display: block; }
  .social span:nth-child(2) { background: #2a5aa0; }
  .social span:nth-child(3) { background: var(--blue); }

  .photo {
    position: absolute;
    border-radius: 50%;
    border: 6px solid rgba(133,202,230,0.75);
  }
  .photo--hero {
    left: 437px; top: 26px; width: 240px; height: 240px;
    background: radial-gradient(circle at 55% 40%, #dfe5ea, #9aa7b4 60%, #3a4f78);
  }
  .photo--before, .photo--after {
    top: 326px; width: 128px; height: 128px;
    background: radial-gradient(circle at 50% 45%, #e7d2bf, #b7a999 55%, #ececec);
  }
  .photo--before { left: 432px; }
  .photo--after { left: 548px; }
  .ba-label { top: 460px; color: var(--white); font-size: 21px; font-weight: 300; }

  /* back */
  .back-shape { position: absolute; left: 0; top: 0; }
  .photo--scene {
    position: absolute; left: 0; top: 0; width: 365px; height: 270px;
    background: linear-gradient(180deg, #cfd6dc 0%, #9fb0bd 40%, #5f7a5a 75%, #3f5e3a 100%);
    clip-path: polygon(0 0, 100% 0, 100% 204px, 0 262px);
  }
  .photo--case1, .photo--case2 {
    top: 250px; width: 132px; height: 132px;
    background: radial-gradient(circle at 50% 45%, #d9c2ae, #6b7e98 60%, #24324a);
  }
  .photo--case1 { left: 44px; }
  .photo--case2 { left: 202px; background: radial-gradient(circle at 50% 45%, #eee, #c8b8a6 55%, #888); }

  .info { left: 30px; top: 400px; color: var(--white); font-size: 12.5px; line-height: 16.5px; }
  .info dl { display: grid; grid-template-columns: 72px auto; }
  .info dt, .info dd { font-weight: 400; }

  .brand--back { left: 392px; top: 66px; }
  .postage {
    left: 585px; top: 24px; width: 96px; height: 94px;
    border: 2px solid #111;
    display: flex; flex-direction: column; align-items: center; justify-content: center;
    font-size: 11px; line-height: 13px; color: #111; text-align: center;
  }
  .postage strong { font-weight: 700; }
  .address-line { left: 398px; width: 288px; height: 1px; background: #777; }
</style>
</head>
<body>

<section class="postcard postcard--front">
  <svg class="front-shape" width="717" height="494" viewBox="0 0 717 494" aria-hidden="true">
    <path d="M506,0 C560,60 560,150 490,230 C420,310 380,380 370,494 L717,494 L717,0 Z" fill="#1b8fc9"/>
    <path d="M560,0 C600,80 590,170 520,250 C460,320 430,400 426,494 L470,494 C472,400 500,330 560,260 C620,190 640,90 600,0 Z" fill="#85cae6" opacity="0.35"/>
  </svg>

  <div class="front-copy">
    <p class="offer">FREE CONSULTATION <strong>+ 50% OFF</strong><br>YOUR FIRST SESSION!</p>
    <h1 class="slogan">Lose Weight. Gain Muscle.</h1>
    <p class="intro">Customized Personal training using Q-Pulse, the latest<br>technology in fitness.</p>
    <p class="goals">REACH YOUR FITNESS GOALS<br><span class="accent">IN JUST 2</span><br><strong>25-MIN SESSIONS PER WEEK!</strong></p>
  </div>

  <div class="brand brand--front abs"><span class="brand-dot"></span>MAPLE STRIDE</div>

  <div class="contact abs">
    <p class="label">For more information</p>
    <p class="phone">(949) 555-0137</p>
    <p class="mail">maplestridehealth@mailbox.example</p>
  </div>
  <div class="social abs" aria-hidden="true"><span></span><span></span><span></span></div>

  <div class="photo photo--hero" role="img" aria-label="Trainer guiding a client through a Q-Pulse session on an exercise ball"></div>
  <div class="photo photo--before" role="img" aria-label="Client before training, flexing arm"></div>
  <div class="photo photo--after" role="img" aria-label="Client after training, flexing arm"></div>
  <p class="ba-label abs" style="left:470px">Before</p>
  <p class="ba-label abs" style="left:590px">After</p>

  <div class="tagline-band">Up to 18 times more effective than a conventional gym workout...</div>
</section>

<section class="postcard postcard--back">
  <svg class="back-shape" width="365" height="494" viewBox="0 0 365 494" aria-hidden="true">
    <path d="M0,262 L365,204 L365,494 L0,494 Z" fill="#1b8fc9"/>
    <path d="M0,340 C120,310 260,330 365,390 L365,494 L0,494 Z" fill="#85cae6" opacity="0.45"/>
  </svg>
  <div class="photo--scene" role="img" aria-label="Two women training with Q-Pulse equipment on a rooftop overlooking a harbor"></div>
  <div class="photo photo--case1" role="img" aria-label="Before and after comparison of a client"></div>
  <div class="photo photo--case2" role="img" aria-label="Before and after side view of a client"></div>

  <div class="info abs">
    <dl>
      <dt>Address:</dt><dd>372 Dovercrest Ave, Building B<br>Suite 218, Costa Mesa CA 92631</dd>
      <dt>Website:</dt><dd>maple-stride.example</dd>
      <dt>Phone #:</dt><dd>(949) 555-0137</dd>
      <dt>E-mail:</dt><dd>maplestridehealth@mailbox.example</dd>
    </dl>
  </div>

  <div class="brand brand--back abs"><span class="brand-dot"></span>MAPLE STRIDE</div>
  <div class="postage abs">
    <span>PRESORTED</span><span>STANDARD</span><span>US POSTAGE</span><strong>PAID</strong><span>ANYTOWN, OH</span><span>PERMIT #0000</span>
  </div>
  <div class="address-line abs" style="top:262px"></div>
  <div class="address-line abs" style="top:334px"></div>
  <div class="address-line abs" style="top:407px"></div>
  <div class="address-line abs" style="top:479px"></div>

  <div class="tagline-band">Up to 18 times more effective than a conventional gym workout...</div>
</section>

</body>
</html>
```